Corvana Wound Care Business card design

We need a business card designed around our logo which was provided. The logo of preference is the colored. Also the colors and fonts were provided.

Target Market(s)

Our Referral partners are home health agencies.

Industry/Entity Type

Healthcare

Contact Information for Business Card

Name , Phone #, Email , Title

Requirements
Nice to have
• Creativity
Should not have
• basic

```html
<!DOCTYPE html>
<html lang="en">
<head>
<meta charset="utf-8">
<title>Corvana Wound Care – Business Card</title>
<link rel="stylesheet" href="https://fonts.googleapis.com/css2?family=Catamaran:wght@500;600;700&display=swap">
<style>
  :root {
    --page: #ebebed;
    --brand-blue: #2b3f94;
    --pattern-light: #3d8fd6;
    --pattern-dark: #2a4fae;
    --ghost: #e6e6e8;
    --white: #ffffff;
    --ink: #111111;
  }
  * { margin: 0; padding: 0; box-sizing: border-box; }
  html, body { width: 1200px; height: 840px; overflow: hidden; }
  body {
    background: var(--page);
    font-family: "Catamaran", sans-serif;
    position: relative;
  }
  .card {
    position: absolute;
    left: 330px;
    width: 539px;
    height: 324px;
    overflow: hidden;
  }
  .card-front { top: 65px; background: var(--brand-blue); }
  .card-back { top: 452px; background: var(--white); }

  .front-pattern {
    position: absolute; left: 0; top: 0; width: 100%; height: 162px;
    background: linear-gradient(180deg, var(--pattern-light) 0%, var(--pattern-dark) 75%, var(--brand-blue) 100%);
    opacity: .85;
  }
  .front-brand {
    position: absolute; left: 0; right: 0; top: 190px;
    text-align: center; color: var(--white);
  }
  .brand-name {
    font-weight: 700; font-size: 40px; line-height: 1; letter-spacing: .5px;
  }
  .brand-sub {
    font-weight: 700; font-size: 9px; letter-spacing: 6px; margin-top: 6px;
  }

  .back-pattern {
    position: absolute; left: 0; top: 0; width: 272px; height: 100%;
    background: linear-gradient(90deg, var(--ghost) 0%, #f2f2f3 70%, var(--white) 100%);
  }
  .back-brand {
    position: absolute; left: 30px; top: 136px; width: 200px;
    color: var(--brand-blue); text-align: center;
  }
  .back-brand .brand-name { font-size: 28px; }
  .back-brand .brand-sub { font-size: 7px; letter-spacing: 4px; margin-top: 4px; }

  .person {
    position: absolute; right: 37px; top: 40px; text-align: right;
  }
  .person-name {
    color: var(--brand-blue); font-weight: 600; font-size: 24px; line-height: 1;
  }
  .person-title {
    color: var(--ink); font-weight: 600; font-size: 13px; line-height: 1; margin-top: 6px;
  }
  .icon-rail {
    position: absolute; left: 236px; top: 108px; width: 40px; height: 166px;
    background: var(--brand-blue); border-radius: 10px;
  }
  .contact-list {
    position: absolute; left: 300px; top: 120px; list-style: none;
    color: var(--ink); font-weight: 600; font-size: 18px; line-height: 24px;
  }
  .contact-web { margin-top: 11px; }
</style>
</head>
<body>
  <section class="card card-front">
    <div class="front-pattern" role="img" aria-label="Repeating pattern of blue medical crosses"></div>
    <div class="front-brand">
      <div class="brand-name">Corvana</div>
      <div class="brand-sub">WOUND CARE</div>
    </div>
  </section>

  <section class="card card-back">
    <div class="back-pattern" role="img" aria-label="Faint pattern of pale grey medical crosses"></div>
    <div class="back-brand">
      <div class="brand-name">Corvana</div>
      <div class="brand-sub">WOUND CARE</div>
    </div>

    <div class="person">
      <div class="person-name">MARISOL KEANE</div>
      <div class="person-title">Certified Wound Care Specialist</div>
    </div>

    <svg class="icon-rail" viewBox="0 0 40 166" aria-hidden="true">
      <path d="M13 12c-2 2-2 5 0 9l6 7c4 4 7 5 9 3l2-2-4-4-3 2-6-6 2-3-4-4z" fill="none" stroke="#fff" stroke-width="2"/>
      <path d="M20 50c-5 0-8 4-8 8 0 6 8 14 8 14s8-8 8-14c0-4-3-8-8-8z" fill="#fff"/>
      <circle cx="20" cy="58" r="3" fill="#2b3f94"/>
      <rect x="6" y="91" width="28" height="18" fill="none" stroke="#fff" stroke-width="1.8"/>
      <path d="M6 91l14 11 14-11M6 109l11-9M34 109l-11-9" fill="none" stroke="#fff" stroke-width="1.4"/>
      <circle cx="19" cy="136" r="11" fill="none" stroke="#fff" stroke-width="1.6"/>
      <path d="M8 136h22M19 125v22M12 129h14M12 143h14" stroke="#fff" stroke-width="1.2"/>
      <ellipse cx="19" cy="136" rx="5" ry="11" fill="none" stroke="#fff" stroke-width="1.2"/>
      <path d="M25 139l8 8-3 1 2 3-2 1-2-3-3 2z" fill="#fff" stroke="#2b3f94" stroke-width=".8"/>
    </svg>

    <ul class="contact-list">
      <li>+1 (469) 555-0148</li>
      <li>1730 Harbor Clinic</li>
      <li>Way, Plano, TX 75074</li>
      <li>care@corvana.com</li>
      <li class="contact-web">www.corvanacare.com</li>
    </ul>
  </section>
</body>
</html>
```